Design Landing Page and User Interface for Online Second Hand Merchandice Store in Web 2.0 type pa

We are creating a company which delivers second hand merchandise locally. We'd like to have a landing page developed in the web 2.0 parallax scrolling web 2.0 style. We have a design style in mind. We need to have other pages within the website designed also. However, we need to get the landing page correct first.

In the center of the landing page, there will be the Second Hand Copper Lantern Copper Lantern logo. Underneath that logo, there will be an entry to enter your email and underneath that entry, there will be an entry to enter your password. Then there will be a login button. This will be the top layer of the landing page and it will be "transparent".

The second layer of the landing page, will be "behind" the logo and login. On this second layer, there will be boxes that will have pictures of items for sale such furniture, ipods, lamps, books, CD's, TV, couches, beds. The boxes will flip over randomly and then the price for the item will be shown on the flip side of the box. If a user clicks on the box to find the price.

Scrolling down the landing Page – When you scroll down the landing page, you will see a little info graphic, which will show you how the service works. This is kind of an emulation of the Wavelore.example website which is pretty clean and looks nice.

At the bottom of the landing page you will have the menu that will have the same items as the Quillnest landing page. This will pretty much allow users to get anywhere they need to in the site. This will also serve as a guide to you to how to design architect and build everything onward from here.

NOTE: THE LANDING PAGE WILL ONLY BE SKETCH PAGES 1-4

Target Market(s)

The customers will be hipsters who live in artsy neighborhoods in the United States. The customers are cost conscious and like to save money, but also appreciate style and are also very tech savvy. The ride bicycles and are into recycling and doing helping the environment.

Industry/Entity Type

Architect

Requirements
Must have
• The website design must have the parallax scrolling style. The landing page must have our company logo on it. The logo of the company name is attached in this brief. The logo reads Second Hand Copper Lantern.

Nice to have
• A cool modern look. Imagine if Flutterbox opened up a Second Hand Goods store. That's what I want it to look like.
Should not have
• An early 2000's or mid 2000's style of design.

```html
<!DOCTYPE html>
<html lang="en">
<head>
<meta charset="utf-8">
<title>Copper Lantern – Buy and sell stuff to people who know people you know</title>
<link rel="stylesheet" href="https://fonts.googleapis.com/css2?family=Open+Sans:wght@300;400;600;700&display=swap">
<style>
:root{
  --teal:#2b8b8c;
  --teal-dark:#1f6d6e;
  --green:#5bb03c;
  --green-dark:#3f8a27;
  --ink:#333b3f;
  --muted:#6d7579;
  --paper:#ffffff;
  --mist:#ececec;
  --line:#d5d8d9;
  --price:#c8372d;
  --login:#2f7fc2;
  --friend:#3b5a98;
  --footer:#2e3133;
  --tile-a:#3b3f44;
  --tile-b:#5a4c3f;
  --tile-c:#2a2d31;
  --tile-d:#6b6f73;
}
*{box-sizing:border-box;margin:0;padding:0}
html,body{width:1200px;height:4288px;overflow:hidden}
body{font-family:"Open Sans",Arial,sans-serif;color:var(--ink);background:var(--paper);position:relative}
section,footer{position:absolute;left:0;width:1200px}

/* Hero */
.hero{top:0;height:1120px;overflow:hidden;background:var(--tile-c)}
.product-wall{position:absolute;inset:0;display:grid;grid-template-columns:repeat(10,120px);grid-auto-rows:124px}
.tile{border:3px solid #1d1f22}
.tile:nth-child(4n+1){background:linear-gradient(135deg,var(--tile-a),var(--tile-c))}
.tile:nth-child(4n+2){background:linear-gradient(135deg,var(--tile-b),var(--tile-a))}
.tile:nth-child(4n+3){background:linear-gradient(135deg,var(--tile-d),var(--tile-c))}
.tile:nth-child(4n){background:linear-gradient(135deg,#4a5058,#23262a)}
.tile.price{background:var(--price);color:#fff;display:flex;flex-direction:column;justify-content:center;align-items:center;font-weight:700;line-height:1.1}
.tile.price span{font-size:20px;letter-spacing:1px}
.tile.price b{font-size:30px}
.hero-shade{position:absolute;inset:0;background:radial-gradient(ellipse at 50% 45%,rgba(255,255,255,.35),rgba(0,0,0,.35) 70%)}
.brand{position:absolute;left:430px;top:70px;width:340px;text-align:center}
.brand-mark{width:220px;height:220px;border-radius:50%;background:var(--teal);margin:0 auto 18px}
.brand-name{font-size:40px;font-weight:700;color:#fff;letter-spacing:1px}
.tagline{position:absolute;left:610px;top:560px;width:300px;color:#fff;font-size:28px;font-weight:600;line-height:1.25}
.btn-login{position:absolute;left:520px;top:700px;width:160px;height:58px;border-radius:6px;background:var(--login);color:#fff;font-size:24px;font-weight:600;text-align:center;line-height:58px}
.btn-friend{position:absolute;left:492px;top:780px;width:216px;height:40px;border-radius:4px;background:var(--friend);color:#fff;font-size:15px;display:flex;align-items:center;gap:10px;padding-left:12px}
.btn-friend i{width:20px;height:20px;background:#fff;display:block}
.scroll-down{position:absolute;left:550px;top:1000px;width:100px;height:100px;border-radius:50%;background:#fff;color:var(--ink);font-size:14px;font-weight:700;text-align:center;padding-top:22px;line-height:1.2}

/* How it works */
.how{top:1120px;height:988px;background:var(--mist)}
.how h2,.neighborhood h2,.benefits h2,.trade h2{font-weight:600;color:var(--ink);text-align:center}
.how h2{font-size:48px;position:absolute;left:0;width:1200px}
.steps{position:absolute;left:140px;width:920px;display:flex;justify-content:space-between}
.step{width:280px;text-align:center}
.step h3{font-size:30px;font-weight:400;color:var(--teal);margin-bottom:20px}
.step h3 b{font-weight:700}
.step svg{display:block;margin:0 auto 22px}
.step p{font-size:15px;color:var(--ink);line-height:1.4;padding:0 40px}
.btn-signup{position:absolute;left:520px;width:160px;height:42px;border-radius:21px;background:var(--green);color:#fff;font-size:16px;font-weight:600;text-align:center;line-height:42px;box-shadow:0 3px 0 var(--green-dark)}

/* Neighborhood */
.neighborhood{top:2108px;height:652px;background:var(--paper)}
.neighborhood h2{font-size:34px;margin-top:52px}
.cycle{position:absolute;left:160px;top:150px}
.cycle-center{position:absolute;left:440px;top:310px;width:320px;text-align:center;color:var(--teal-dark);font-size:24px;font-weight:600;line-height:1.3}
.goods{position:absolute;border-radius:6px}
.cycle-note{position:absolute;font-size:13px;color:var(--muted);width:120px;line-height:1.3}

/* Benefits */
.benefits{top:2760px;height:640px;background:var(--paper);border-top:1px solid var(--line)}
.benefits h2{font-size:38px;margin-top:40px}
.benefit-list{position:absolute;left:100px;top:120px;width:520px;list-style:none;counter-reset:b}
.benefit-list li{font-size:20px;color:var(--ink);margin-bottom:15px;line-height:1.35;counter-increment:b;padding-left:26px;position:relative}
.benefit-list li::before{content:counter(b) ".";position:absolute;left:0;color:var(--teal);font-weight:600}
.faq{position:absolute;left:700px;top:112px;width:460px;height:420px;background:var(--mist);padding:24px 36px}
.faq h3{text-align:center;font-size:32px;font-weight:600;margin-bottom:16px}
.faq dt{color:var(--login);font-size:20px;line-height:1.3}
.faq dd{color:var(--muted);font-size:15px;margin:4px 0 14px;line-height:1.35}

/* Trade post */
.trade{top:3400px;height:800px;background:var(--paper);border-top:1px solid var(--line)}
.trade h2{font-size:40px;margin-top:88px}
.trade-panel{position:absolute;left:180px;top:190px;width:840px;height:520px;display:flex;box-shadow:0 14px 20px -14px rgba(0,0,0,.35)}
.trade-col{flex:1;padding:20px 30px}
.trade-col+.trade-col{border-left:2px solid var(--line)}
.trade-col h3{text-align:center;font-size:28px;font-weight:600;color:var(--teal);margin-bottom:40px}
.field{display:flex;align-items:center;gap:10px;margin-bottom:26px;font-size:13px;color:var(--muted)}
.field label{width:110px;text-align:right}
.input{height:28px;border:1px solid var(--line);border-radius:3px;padding:0 8px;line-height:26px;font-size:12px;color:#9aa0a3;width:170px}
.input.tall{height:96px}
.input.short{width:110px}
.btn-small{height:28px;padding:0 10px;background:var(--teal);color:#fff;font-size:12px;line-height:28px;border-radius:3px}
.btn-sell{display:block;margin:8px auto 0;width:120px;height:34px;border-radius:17px;background:var(--teal);color:#fff;text-align:center;line-height:34px;font-size:14px;font-weight:600}

/* Footer */
.site-footer{top:4200px;height:88px;background:var(--footer);color:#b9bec1;font-size:12px;padding:18px 40px}
.footer-links{display:flex;gap:18px}
.site-footer small{display:block;margin-top:14px;font-size:11px;color:#8d9396}
.social{position:absolute;right:40px;top:22px;display:flex;gap:10px}
.social i{width:24px;height:24px;background:#5a5f62;display:block}
</style>
</head>
<body>

<section class="hero">
  <div class="product-wall" role="img" aria-label="Wall of photo tiles showing second hand goods for sale: laptops, phones, music players and books, some flipped to show prices">
    <div class="tile"></div><div class="tile"></div><div class="tile"></div><div class="tile"></div><div class="tile"></div><div class="tile"></div><div class="tile"></div><div class="tile"></div><div class="tile price"><span>PRICE</span><b>$239</b></div><div class="tile"></div>
    <div class="tile"></div><div class="tile"></div><div class="tile"></div><div class="tile"></div><div class="tile"></div><div class="tile"></div><div class="tile"></div><div class="tile"></div><div class="tile"></div><div class="tile"></div>
    <div class="tile"></div><div class="tile price"><span>PRICE</span><b>$239</b></div><div class="tile"></div><div class="tile"></div><div class="tile"></div><div class="tile"></div><div class="tile"></div><div class="tile"></div><div class="tile"></div><div class="tile"></div>
    <div class="tile"></div><div class="tile"></div><div class="tile"></div><div class="tile"></div><div class="tile"></div><div class="tile"></div><div class="tile"></div><div class="tile"></div><div class="tile"></div><div class="tile"></div>
    <div class="tile"></div><div class="tile"></div><div class="tile"></div><div class="tile"></div><div class="tile"></div><div class="tile"></div><div class="tile"></div><div class="tile"></div><div class="tile"></div><div class="tile"></div>
    <div class="tile"></div><div class="tile"></div><div class="tile"></div><div class="tile"></div><div class="tile"></div><div class="tile"></div><div class="tile"></div><div class="tile"></div><div class="tile price"><span>PRICE</span><b>$239</b></div><div class="tile"></div>
    <div class="tile"></div><div class="tile price"><span>PRICE</span><b>$239</b></div><div class="tile"></div><div class="tile"></div><div class="tile"></div><div class="tile"></div><div class="tile"></div><div class="tile"></div><div class="tile"></div><div class="tile"></div>
    <div class="tile"></div><div class="tile"></div><div class="tile"></div><div class="tile"></div><div class="tile"></div><div class="tile"></div><div class="tile"></div><div class="tile"></div><div class="tile"></div><div class="tile"></div>
    <div class="tile"></div><div class="tile"></div><div class="tile"></div><div class="tile"></div><div class="tile"></div><div class="tile"></div><div class="tile"></div><div class="tile"></div><div class="tile"></div><div class="tile"></div>
  </div>
  <div class="hero-shade"></div>
  <div class="brand">
    <div class="brand-mark"></div>
    <div class="brand-name">Copper Lantern</div>
  </div>
  <p class="tagline">Buy and sell stuff to people who know people you know</p>
  <div class="btn-login">Log In</div>
  <div class="btn-friend"><i></i>Login with Friendlink</div>
  <div class="scroll-down">SCROLL<br>DOWN<br>&#8964;</div>
</section>

<section class="how">
  <h2 style="top:48px">How It Works To Sell</h2>
  <div class="steps" style="top:160px">
    <div class="step">
      <h3>Post <b>Stuff</b></h3>
      <svg width="72" height="72" viewBox="0 0 72 72"><path d="M8 22 36 10 64 22 64 58 36 68 8 58Z" fill="var(--teal)"/><path d="M8 22 36 34 64 22M36 34V68" stroke="#fff" stroke-width="3" fill="none"/></svg>
      <p>Post Your Stuff to Sell on Your Trading Post Page</p>
    </div>
    <div class="step">
      <h3>Get <b>Offers</b></h3>
      <svg width="72" height="72" viewBox="0 0 72 72"><circle cx="36" cy="36" r="30" fill="none" stroke="var(--teal)" stroke-width="5"/><circle cx="26" cy="29" r="4" fill="var(--teal)"/><circle cx="46" cy="29" r="4" fill="var(--teal)"/><path d="M22 42q14 14 28 0" stroke="var(--teal)" stroke-width="5" fill="none"/></svg>
      <p>Get Instant Offers on your stuff for Free</p>
    </div>
    <div class="step">
      <h3>Pickup <b>Service</b></h3>
      <svg width="84" height="72" viewBox="0 0 84 72"><rect x="4" y="16" width="46" height="36" fill="var(--teal)"/><path d="M52 26h16l12 14v12H52Z" fill="var(--teal)"/><circle cx="20" cy="58" r="8" fill="var(--teal)" stroke="#fff" stroke-width="3"/><circle cx="66" cy="58" r="8" fill="var(--teal)" stroke="#fff" stroke-width="3"/></svg>
      <p>The Trade Post Will Pick up Your stuff</p>
    </div>
  </div>
  <div class="btn-signup" style="top:420px">Sign up Now</div>

  <h2 style="top:520px">How It Works To Buy</h2>
  <div class="steps" style="top:630px">
    <div class="step">
      <h3>Browse <b>Stuff</b></h3>
      <svg width="72" height="80" viewBox="0 0 72 80"><path d="M10 6h36l16 16v52H10Z" fill="none" stroke="var(--teal)" stroke-width="5"/><path d="M20 34h32M20 46h32M20 58h20" stroke="var(--teal)" stroke-width="4"/></svg>
      <p>Browse by section, Key Word or Sale Urgency</p>
    </div>
    <div class="step">
      <h3>Bid <b>Offers</b></h3>
      <svg width="80" height="80" viewBox="0 0 80 80"><ellipse cx="30" cy="60" rx="22" ry="8" fill="var(--teal)"/><ellipse cx="30" cy="50" rx="22" ry="8" fill="var(--teal)" stroke="#fff" stroke-width="2"/><ellipse cx="30" cy="40" rx="22" ry="8" fill="var(--teal)" stroke="#fff" stroke-width="2"/><circle cx="58" cy="30" r="18" fill="var(--teal)"/><text x="58" y="37" font-size="20" font-weight="700" text-anchor="middle" fill="#fff" font-family="Open Sans,sans-serif">$</text></svg>
      <p>Buy or Place Bid. Get response back Within Preselected Time</p>
    </div>
    <div class="step">
      <h3>Setup <b>Delivery</b></h3>
      <svg width="72" height="80" viewBox="0 0 72 80"><rect x="6" y="12" width="60" height="62" rx="4" fill="none" stroke="var(--teal)" stroke-width="5"/><rect x="6" y="12" width="60" height="14" fill="var(--teal)"/><path d="M20 4v14M52 4v14" stroke="var(--teal)" stroke-width="5"/><g fill="var(--teal)"><rect x="16" y="34" width="10" height="9"/><rect x="31" y="34" width="10" height="9"/><rect x="46" y="34" width="10" height="9"/><rect x="16" y="52" width="10" height="9"/><rect x="31" y="52" width="10" height="9"/></g></svg>
      <p>Setup Time for delivery and Review stuff</p>
    </div>
  </div>
  <div class="btn-signup" style="top:905px">Sign up Now</div>
</section>

<section class="neighborhood">
  <h2>Neighborhood Economics Benefits Your Neighborhood</h2>
  <svg class="cycle" width="880" height="440" viewBox="0 0 880 440">
    <ellipse cx="440" cy="220" rx="330" ry="150" fill="none" stroke="var(--line)" stroke-width="3"/>
    <g fill="var(--line)">
      <path d="M430 64l16 6-16 6z"/><path d="M760 230l-6 16-6-16z"/><path d="M450 376l-16-6 16-6z"/><path d="M120 210l6-16 6 16z"/>
    </g>
  </svg>
  <div class="goods" role="img" aria-label="Smartphone" style="left:180px;top:180px;width:60px;height:110px;background:linear-gradient(#4a4f55,#1c1e21)"></div>
  <div class="goods" role="img" aria-label="Flat screen television" style="left:840px;top:190px;width:170px;height:110px;background:linear-gradient(#2c3036,#0f1113)"></div>
  <div class="goods" role="img" aria-label="Wooden coffee table" style="left:860px;top:530px;width:150px;height:60px;background:linear-gradient(#6a3f28,#3e2416)"></div>
  <div class="goods" role="img" aria-label="Upright vacuum cleaner" style="left:180px;top:470px;width:90px;height:130px;background:linear-gradient(#3a5fb0,#1f3a7a)"></div>
  <div class="cycle-note" style="left:470px;top:168px">Uses that fund to Buy pocket phone</div>
  <div class="cycle-note" style="left:910px;top:320px">Sells Old TV</div>
  <div class="cycle-note" style="left:620px;top:540px">Uses that fund to Buy Coffee Table</div>
  <div class="cycle-note" style="left:130px;top:340px">Sells Old Vacuum</div>
  <div class="cycle-center">Buy and sell stuff in minutes instead of days</div>
</section>

<section class="benefits">
  <h2>Benefits of Buying &amp; Selling on Travel Post</h2>
  <ol class="benefit-list">
    <li>Buy Faster and Sell Faster</li>
    <li>Sellers with Good History get Paid Faster</li>
    <li>Buy Faster and Sell Faster</li>
    <li>Participate in a Local Community of Vertical Buyers and Sellers</li>
    <li>Buy Faster and Sell Faster</li>
    <li>Sellers with Good History get Paid Faster</li>
    <li>Buy Faster and Sell Faster</li>
    <li>Participate in a Local Community of Vertical Buyers and Sellers</li>
  </ol>
  <dl class="faq">
    <h3>F.A.Q</h3>
    <dt>Q.1 How is this different than Boardly or Bidmart ?</dt>
    <dd>Ans. It's Safer, Quicker, Reliable and Privacy of Buyer and Seller.</dd>
    <dt>Q.1 How is this different than Boardly or Bidmart ?</dt>
    <dd>Ans. It's Safer, Quicker, Reliable and Privacy of Buyer and Seller.</dd>
    <dt>Q.1 How is this different than Boardly or Bidmart ?</dt>
    <dd>Ans. It's Safer, Quicker, Reliable and Privacy of Buyer and Seller.</dd>
  </dl>
  <div class="btn-signup" style="top:560px">Sign up Now</div>
</section>

<section class="trade">
  <h2>My Trade Party Post Page</h2>
  <div class="trade-panel">
    <div class="trade-col">
      <h3>Buy Stuff</h3>
      <div class="field"><label>Search For:</label><span class="input">Coffee Table</span><span class="btn-small">Search</span></div>
      <div class="field"><label>Search By Category:</label><span class="input">Furniture</span><span class="btn-small">Search</span></div>
    </div>
    <div class="trade-col">
      <h3>Sell Stuff</h3>
      <div class="field"><label>Item Category:</label><span class="input">Coffee Table</span></div>
      <div class="field"><label>List under:</label><span class="input">Registered</span></div>
      <div class="field" style="align-items:flex-start"><label>Describe Item:</label><span class="input tall"></span></div>
      <div class="field"><label>Take Picture:</label>
        <svg width="30" height="24" viewBox="0 0 30 24"><rect x="1" y="5" width="28" height="18" rx="3" fill="var(--muted)"/><rect x="9" y="1" width="12" height="6" fill="var(--muted)"/><circle cx="15" cy="14" r="5" fill="#fff"/></svg>
      </div>
      <div class="field"><label>Set Price:</label><span class="input short">$350.00</span></div>
      <span class="btn-sell">Sell Item</span>
    </div>
  </div>
</section>

<footer class="site-footer">
  <nav class="footer-links"><span>About Copper Lantern</span><span>|</span><span>Latest News</span><span>|</span><span>Sign up to the Newsletter</span><span>|</span><span>Trade Commodities Market Analysis in your Home</span></nav>
  <small>Copper Lantern © 2014. All rights reserved.</small>
  <div class="social"><i></i><i></i><i></i><i></i></div>
</footer>

</body>
</html>
```